Label Design - Hair & Beauty Care Wholesaler

Design a label for our client that demonstrates your design skills, your eye for detail and your ability to respond well to the type of brief we produce.

We are offering one prize for the winning design and two participation prizes. The winner will also receive 20 laminated polypropylene labels from the first production run for their portfolio.

Note: This is a test project for us and we know there is a lot of talent out there! Even if you don't win this time, we may be able to engage you for other projects, so if you have the skills and interest we would encourage you to submit a design to make sure we know about you.

One submission only per designer only please.

PROJECT

Our client runs a successful, long-established wholesale hair and beauty care business. Among other things, they sell products like shampoos and conditioners in bulk-buy containers, which hairdressers buy to use in-store in their salons.

(Depending on where you are, the type of product our client needs labels for may be known as a “store brand”, “house brand”, “private label brand”, “own brand”, “home brand” or “generic brand”.)

For this project, the content for the first label to be produced is attached. Keep in mind we will need to be able to change the product name, volume/quantity and ingredients for other labels in future.

Ask questions if you need to! Thanks for participating.

Target Market(s)

Hairdressers and beauty salon owners in Australia.

Industry/Entity Type

Business

Requirements
Must have
• Client's existing logo
All text in the attached "Content" file
Rectangular shape with rounded corners
Finished size 75mm width x 145mm height

```html
<!DOCTYPE html>
<html lang="en">
<head>
<meta charset="utf-8">
<title>Lanolin Shampoo Label</title>
<link rel="stylesheet" href="https://fonts.googleapis.com/css2?family=Raleway:wght@300;400&family=Arimo:wght@400;700&display=swap">
<style>
  :root {
    --page: #ffffff;
    --maroon: #7b1f46;
    --maroon-light: #8b3459;
    --leaf: #8fb43c;
    --leaf-dark: #5f8a24;
    --brand-red: #c8283a;
    --ink-light: #ffffff;
  }
  html, body {
    margin: 0;
    padding: 0;
    width: 800px;
    height: 1200px;
    overflow: hidden;
    background: var(--page);
  }
  .canvas {
    position: relative;
    width: 800px;
    height: 1200px;
  }
  .label {
    position: absolute;
    left: 186px;
    top: 170px;
    width: 430px;
    height: 870px;
    border-radius: 26px;
    background: var(--maroon);
    overflow: hidden;
    color: var(--ink-light);
  }
  .label__arcs {
    position: absolute;
    inset: 0;
  }
  .brand {
    position: absolute;
    top: 32px;
    left: 0;
    right: 0;
    display: flex;
    justify-content: center;
    align-items: center;
    gap: 8px;
  }
  .brand__mark {
    width: 14px;
    height: 14px;
    background: var(--brand-red);
  }
  .brand__name {
    font-family: "Arimo", Arial, sans-serif;
    font-weight: 700;
    font-size: 18px;
    letter-spacing: 2px;
    color: var(--ink-light);
  }
  .product-name {
    position: absolute;
    top: 160px;
    left: 0;
    right: 0;
    margin: 0;
    text-align: center;
    font-family: "Raleway", sans-serif;
    font-weight: 300;
    font-size: 70px;
    line-height: 1;
    letter-spacing: 4px;
    color: var(--ink-light);
  }
  .product-swoosh {
    position: absolute;
    top: 236px;
    left: 80px;
    width: 290px;
    height: 12px;
  }
  .product-type {
    position: absolute;
    top: 256px;
    left: 0;
    right: 0;
    margin: 0;
    text-align: center;
    font-family: "Raleway", sans-serif;
    font-weight: 400;
    font-size: 30px;
    letter-spacing: 4px;
    color: var(--ink-light);
  }
  .emblem-area {
    position: absolute;
    left: 130px;
    top: 398px;
    width: 170px;
    height: 206px;
    border-radius: 18px;
    background: linear-gradient(160deg, var(--leaf), var(--leaf-dark));
    opacity: 0.85;
  }
  .volume {
    position: absolute;
    top: 638px;
    right: 52px;
    margin: 0;
    font-family: "Arimo", Arial, sans-serif;
    font-weight: 700;
    font-size: 29px;
    color: var(--leaf);
  }
  .ingredients {
    position: absolute;
    top: 694px;
    left: 10px;
    right: 10px;
    margin: 0;
    text-align: center;
    font-family: "Arimo", Arial, sans-serif;
    font-weight: 700;
    font-size: 10.5px;
    line-height: 15px;
    color: var(--ink-light);
  }
  .ingredients span {
    display: block;
    white-space: nowrap;
  }
  .contact {
    position: absolute;
    top: 796px;
    left: 10px;
    right: 10px;
    margin: 0;
    text-align: center;
    font-family: "Arimo", Arial, sans-serif;
    font-weight: 700;
    font-size: 10px;
    line-height: 16px;
    color: var(--ink-light);
  }
  .contact span {
    display: block;
    white-space: nowrap;
  }
</style>
</head>
<body>
<div class="canvas">
  <div class="label">
    <svg class="label__arcs" viewBox="0 0 430 870" aria-hidden="true">
      <circle cx="-120" cy="330" r="420" fill="var(--maroon-light)" opacity="0.45"/>
      <circle cx="560" cy="840" r="330" fill="var(--maroon-light)" opacity="0.45"/>
    </svg>

    <div class="brand">
      <span class="brand__mark"></span>
      <span class="brand__name">PARKLINE</span>
    </div>

    <h1 class="product-name">LANOLIN</h1>
    <svg class="product-swoosh" viewBox="0 0 290 12" aria-hidden="true">
      <path d="M0 6 Q145 -2 290 6 Q145 12 0 6 Z" fill="var(--leaf)"/>
    </svg>
    <h2 class="product-type">SHAMPOO</h2>

    <div class="emblem-area" role="img" aria-label="Green product emblem artwork"></div>

    <p class="volume">5 litres</p>

    <p class="ingredients">
      <span>Purified Water, Sodium Laureth Sulphate, Sodium Chloride,</span>
      <span>Cocoamide DEA, Cocoamidopropyl Hydroxysultaine, Panthenol,</span>
      <span>PEG-20 Lanolin, Disodium EDTA, Sodium Hydroxymethyl Glycinate,</span>
      <span>Citric Acid, Perfume</span>
    </p>

    <p class="contact">
      <span>www.parklinehairandbeauty.com.au</span>
      <span>Parkline Hair and Beauty Supplies, Unit 8, 142 Harbour Street, Ashfield NSW 2131</span>
    </p>
  </div>
</div>
</body>
</html>
```